Lunvaro Food Cafeteria and Food Services

I´m a Mexican Company , I dont know if we can built a US web page, but what we are a Cafeteria and Food Services, basically for industry , we produce food at companies for their employes, I have a Brochure to share if you consider. Our logo was made by your team. We need to have a Web page for our potentials custumers find us easy by internet

Target Market(s)

Food for manufacturers /Industry

Industry/Entity Type

Manufacturer

Number of Pages Required

4 page

Font styles to use
Sans Serif

Requirements
Must have
• Great images, Spanish and English options, our mision , vision , our actual customers , (be able to remove it also), our Certifications, our actual packages for services, our 90 days menu, our catering services, Contact page , Cafeteria Services , our meals serve now .
Nice to have
• Great pics, easy to access , and easy to move into the web page, nutricional ideas.
Should not have
• Fluorescent Color , or brilliant

```html
<!DOCTYPE html>
<html lang="es">
<head>
<meta charset="utf-8">
<title>Lunvaro — Servicio de Snack o Cafetería</title>
<link href="https://fonts.googleapis.com/css2?family=Roboto:wght@300;400;500&display=swap" rel="stylesheet">
<style>
  :root {
    --black: #0b0a0a;
    --orange: #f3793d;
    --orange-light: #f6956a;
    --green: #1fbf0a;
    --maroon: #4a0e12;
    --white: #ffffff;
  }
  * { margin: 0; padding: 0; box-sizing: border-box; }
  html, body { width: 1024px; height: 1200px; overflow: hidden; }
  body { position: relative; background: var(--white); font-family: "Roboto", Arial, sans-serif; color: var(--white); }

  .waves { position: absolute; left: 0; top: 0; width: 1024px; height: 1200px; }

  .site-header { position: absolute; left: 0; top: 0; width: 1024px; height: 73px; background: var(--black); }
  .brand-tab {
    position: absolute; left: 59px; top: 0; width: 133px; height: 122px;
    background: var(--white); border-radius: 0 0 50% 50% / 0 0 14px 14px;
    display: flex; flex-direction: column; align-items: center; justify-content: center;
    color: var(--maroon); font-weight: 500; text-align: center;
  }
  .brand-tab .mark { width: 14px; height: 14px; border-radius: 50%; background: var(--green); margin-bottom: 8px; }
  .brand-tab .name { font-size: 22px; line-height: 1; }
  .brand-tab .tag { font-size: 8px; margin-top: 4px; }

  .utility { position: absolute; top: 1px; left: 775px; font-size: 11px; font-weight: 300; display: flex; gap: 20px; align-items: center; }
  .utility span { display: flex; align-items: center; gap: 8px; }
  .utility svg { fill: var(--white); }

  .main-nav { position: absolute; top: 30px; left: 0; width: 1024px; font-size: 14px; }
  .main-nav a { position: absolute; color: var(--white); text-decoration: none; }
  .main-nav a.active::after { content: ""; position: absolute; left: 50%; bottom: -7px; width: 16px; height: 2px; margin-left: -8px; background: var(--orange); }

  .hero { position: absolute; left: 0; top: 108px; width: 1024px; text-align: center; }
  .hero h1 { font-size: 28px; font-weight: 400; }
  .hero .rule { width: 50px; height: 2px; background: var(--white); margin: 14px auto 0; }
  .hero p { width: 518px; margin: 25px auto 0; font-size: 13.5px; line-height: 17px; font-weight: 400; }

  .service-cols { position: absolute; top: 400px; left: 196px; display: flex; color: var(--maroon); }
  .service-col { width: 404px; }
  .service-col h2 { font-size: 23px; font-weight: 500; margin-bottom: 30px; }
  .service-col ul { list-style: none; font-size: 23px; line-height: 28.5px; font-weight: 500; }

  .contact-btn { position: absolute; left: 444px; top: 659px; width: 134px; height: 28px; border: 1px solid var(--orange); color: var(--orange); font-size: 14px; text-align: center; line-height: 26px; text-decoration: none; }

  .contents { position: absolute; left: 0; top: 772px; width: 1024px; text-align: center; }
  .contents h2 { font-size: 27px; font-weight: 500; }
  .contents-table { position: absolute; top: 76px; left: 84px; width: 848px; font-size: 23px; line-height: 28.5px; font-weight: 500; }
  .contents-table .row { position: relative; height: 28.5px; }
  .contents-table span { position: absolute; }
  .contents .note { position: absolute; top: 180px; left: 0; width: 1024px; font-size: 13.5px; font-weight: 500; }

  .site-footer { position: absolute; left: 0; top: 987px; width: 1024px; height: 213px; background: var(--black); text-align: center; }
  .footer-brand { margin-top: 26px; display: flex; flex-direction: column; align-items: center; font-weight: 500; }
  .footer-brand .mark { width: 12px; height: 12px; border-radius: 50%; border: 2px solid var(--white); margin-bottom: 6px; }
  .footer-brand .name { font-size: 20px; line-height: 1; }
  .footer-brand .tag { font-size: 7px; margin-top: 3px; }
  .social { display: flex; justify-content: center; gap: 34px; margin-top: 20px; }
  .social span { width: 12px; height: 12px; border-radius: 50%; background: var(--white); }
  .footer-nav { display: flex; justify-content: center; gap: 27px; margin-top: 17px; font-size: 11.5px; font-weight: 300; }
  .footer-nav a { color: var(--white); text-decoration: none; }
  .address { margin-top: 16px; font-size: 11px; font-weight: 300; line-height: 14px; }
</style>
</head>
<body>
  <svg class="waves" viewBox="0 0 1024 1200" aria-hidden="true">
    <defs>
      <clipPath id="heroClip"><path d="M0 73 H1024 V243 Q520 330 0 300 Z"/></clipPath>
      <clipPath id="contentClip"><path d="M0 806 Q480 705 1024 748 V990 H0 Z"/></clipPath>
    </defs>
    <g clip-path="url(#heroClip)">
      <rect x="0" y="73" width="1024" height="260" fill="var(--orange)"/>
      <circle cx="560" cy="180" r="420" fill="var(--orange-light)" opacity="0.55"/>
      <circle cx="920" cy="120" r="300" fill="var(--orange-light)" opacity="0.5"/>
    </g>
    <path d="M0 303 Q480 330 1024 272 L1024 287 Q520 358 0 310 Z" fill="var(--green)"/>

    <g clip-path="url(#contentClip)">
      <rect x="0" y="700" width="1024" height="290" fill="var(--orange-light)"/>
      <circle cx="800" cy="860" r="480" fill="var(--orange)" opacity="0.9"/>
      <circle cx="120" cy="870" r="260" fill="var(--orange-light)"/>
    </g>
    <path d="M0 765 Q500 680 1024 742 L1024 748 Q500 705 0 780 Z" fill="var(--green)"/>
  </svg>

  <header class="site-header">
    <div class="brand-tab">
      <span class="mark"></span>
      <span class="name">Lunvaro</span>
      <span class="tag">Cafeteria and Food Services</span>
    </div>
    <div class="utility">
      <span><svg width="11" height="10" viewBox="0 0 11 10"><path d="M1 0h1v10H1zM2 1h8l-2 2.5 2 2.5H2z"/></svg>Español ⌄</span>
      <span><svg width="10" height="10" viewBox="0 0 10 10"><path d="M2 0l2 2.5-1 1.3c.7 1.3 1.6 2.2 2.9 2.9l1.3-1L10 8 8.6 9.6C4.5 9.4.6 5.5.4 1.4z"/></svg>(555) 214 7309</span>
    </div>
    <nav class="main-nav">
      <a style="left:388px">Home</a>
      <a style="left:479px">About Us</a>
      <a class="active" style="left:596px">Services</a>
      <a style="left:713px">Customers</a>
      <a style="left:841px">Contact Us</a>
    </nav>
  </header>

  <section class="hero">
    <h1>Servicio de Snack o Cafetería</h1>
    <div class="rule"></div>
    <p>Además, contamos también con área de cafetería en la cual usted podrá encontrar una gran variedad de dulces, chocolates, aguas frescas (naturales), sodas, agua embotellada, jugos de diferentes sabores, papitas, galletas, panecitos, ensaladas de frutas, comida fría (tortas, sandwiches, ensaladas, pizzas, hot dogs, etc.).</p>
  </section>

  <section class="service-cols">
    <div class="service-col">
      <h2>SERVICIO DE CAFETERIA</h2>
      <ul><li>detalle del servicio</li><li>item 1</li><li>item 2</li><li>item 3</li><li>item 4</li></ul>
    </div>
    <div class="service-col">
      <h2>SERVICIO DE SNACK</h2>
      <ul><li>detalle del servicio</li><li>item 1</li><li>item 2</li><li>item 3</li><li>item 4</li></ul>
    </div>
  </section>

  <a class="contact-btn">Contactar</a>

  <section class="contents">
    <h2>CONTENIDO DEL SERVICIO</h2>
    <div class="contents-table">
      <div class="row"><span style="left:0">ITEM 1</span><span style="right:469px">20 grs.</span><span style="left:464px">ITEM 3</span><span style="right:0">20 grs.</span></div>
      <div class="row"><span style="left:0">ITEM 2</span><span style="right:469px">75 grs.</span><span style="left:464px">ITEM 4</span><span style="right:0">75 grs.</span></div>
    </div>
    <p class="note">TODAS LAS RECOMENDACIONES SON BIEN RECIBIDAS Y ADAPTADAS A SUS NECESIDADES</p>
  </section>

  <footer class="site-footer">
    <div class="footer-brand">
      <span class="mark"></span>
      <span class="name">Lunvaro</span>
      <span class="tag">Cafeteria and Food Services</span>
    </div>
    <div class="social"><span></span><span></span><span></span></div>
    <nav class="footer-nav"><a>Home</a><a>About Us</a><a>Services</a><a>Customers</a><a>Contact Us</a></nav>
    <p class="address">Avenida Los Robles 482 Col. Jardines, Valle Norte B. C.<br>Tel. (555) 214 7309</p>
  </footer>
</body>
</html>
```